New Company Website

Need a new website for my company Marlow Greenery.
Marlow Greenery offers four business lines: Interior Landscaping, Urbanscaping, Holiday Decorating, and Rental Plants.
Interior Landscaping is the interior installation and maintenance of live plants and flowers in corporate offices. Interiorscape contracts will be for a variety of terms from month to month to 3 years with differing price points in each option.
Urbanscaping refers to landscaping in the urban environment and is restricted in this definition to street side planters and medians, monument plantings and rooftop/balcony gardens.
Holiday Decorating is the Christmas/Hanukkah decorating during the winter season for corporate offices. The model for this business is to lease decorations for a period of 3 years.
Plant rentals is the short term rental of plants and live flowers (orchids, kalanchoe, etc) to event venues. The long term plan is to become the exclusive interior plant vendor for tradeshow organizations in the Tri-State area.

Target Market(s)

Office Managers, Building Managers, Event Coordinators

Industry/Entity Type

Landscaping

Requirements
Must have
• I love my logo. Please incorporate and use colors. Do not change logo.
Nice to have
• These are my competitors:
www.leafhollowdesigns.example
www.verdalo.example

```html
<!DOCTYPE html>
<html lang="en">
<head>
<meta charset="utf-8">
<title>Marlow Greenery</title>
<link href="https://fonts.googleapis.com/css2?family=Carlito:wght@400;700&family=Arimo:wght@400;700&display=swap" rel="stylesheet">
<style>
:root{
  --brand:#0a5a96;
  --brand-dark:#063e6a;
  --brand-light:#1e8fd8;
  --nav-bg:#c9dced;
  --nav-text:#3a4450;
  --ink:#333a40;
  --muted:#5c6670;
  --sub:#6e8aa6;
  --page:#eceeef;
  --panel:#ffffff;
  --hero-tint:#e2edf8;
  --frame:#4a87b8;
  --rule:#d8dde2;
}
*{margin:0;padding:0;box-sizing:border-box}
html,body{width:1109px;height:1200px;overflow:hidden}
body{position:relative;background:linear-gradient(#f7f7f7 0,#e9ebec 130px,var(--page) 100%);font-family:"Arimo",Arial,sans-serif;color:var(--ink)}
.abs{position:absolute}
.header{left:0;top:0;width:1109px;height:120px;background:linear-gradient(#fbfbfb,#f0f1f2);border-bottom:1px solid #e0e2e4}
.brand{left:165px;top:62px;display:flex;align-items:center;gap:8px}
.brand-mark{width:22px;height:22px;background:var(--brand);border-radius:50%}
.brand-name{font-family:"Carlito",sans-serif;font-weight:700;font-size:24px;color:var(--brand)}
.utility{right:169px;top:16px;font-size:9.5px;color:#333}
.callout{right:168px;top:40px;font-family:"Carlito",sans-serif;font-size:22px;font-weight:700;color:var(--brand)}
.callout span{color:#111}
.search{right:168px;top:83px;display:flex;align-items:center;gap:6px;font-size:9.5px;font-weight:700;color:#333}
.search-field{width:145px;height:17px;border:1px solid #d6d8da;background:#fff;font-weight:400;color:#999;padding:2px 8px;font-size:9px}
.search-go{width:29px;height:17px;background:var(--brand);color:#fff;border-radius:3px;text-align:center;line-height:17px;font-size:9.5px}
.nav{left:166px;top:136px;height:34px;display:flex;gap:4px}
.nav-item{height:34px;background:var(--nav-bg);border-radius:3px;font-family:"Carlito",sans-serif;font-weight:700;font-size:11px;color:var(--nav-text);display:flex;align-items:center;justify-content:center}
.nav-item.active{background:linear-gradient(#0d5f9c,#06406c);color:#fff}
.panel{left:165px;top:185px;width:779px;height:788px;background:var(--panel);border-radius:6px;box-shadow:0 1px 4px rgba(0,0,0,.18)}
.hero-photo{left:171px;top:191px;width:388px;height:244px;background:linear-gradient(135deg,#6d8a4a 0%,#e9e1d0 40%,#d9642a 65%,#f2eee6 100%)}
.hero-copy{left:559px;top:191px;width:379px;height:244px;background:linear-gradient(#eaf3fc,var(--hero-tint))}
.hero-kicker{left:610px;top:228px;font-size:17px;color:#333}
.hero-title{left:610px;top:248px;font-size:24px;font-weight:700;color:#222}
.hero-text{left:611px;top:284px;width:290px;font-size:10.5px;line-height:14.6px;color:#333}
.hero-btn{left:606px;top:372px;width:244px;height:26px;border-radius:13px;background:linear-gradient(#5a6d7e,#2a3a48);color:#fff;font-size:10.5px;font-weight:700;display:flex;align-items:center;padding-left:33px}
.hero-btn svg{position:absolute;right:7px;top:6px}
.tagline{left:165px;width:779px;top:452px;text-align:center;font-family:"Carlito",sans-serif;font-weight:700;font-size:33px;color:#2d2d2d}
.subline{left:165px;width:779px;top:490px;text-align:center;font-family:"Carlito",sans-serif;font-size:21px;color:var(--sub)}
.steps{left:189px;top:537px;width:725px;height:89px;background:#f3f4f5;border:1px solid var(--rule);border-radius:4px}
.steps-lead{left:255px;width:200px;top:555px;text-align:center;font-family:"Carlito",sans-serif;font-weight:700;font-size:22px;color:var(--brand);line-height:27px}
.steps-lead span{color:#222}
.steps svg{position:absolute;left:0;top:0}
.projects-title{left:188px;top:640px;font-family:"Carlito",sans-serif;font-weight:700;font-size:18.5px;color:var(--brand)}
.projects-text{left:190px;top:670px;width:724px;font-size:10.4px;line-height:13px;color:#555}
.shot{top:734px;width:132px;height:175px;border:4px solid var(--frame);border-radius:2px}
.divider{top:725px;width:1px;height:197px;background:var(--rule)}
.cta{left:492px;top:925px;width:125px;height:26px;background:var(--brand);color:#fff;font-size:10.5px;font-weight:700;text-align:center;line-height:26px}
.services{left:165px;top:975px;width:779px;height:162px;background:rgba(255,255,255,.35)}
.services-title{left:198px;top:989px;font-size:16px;font-weight:700;color:var(--brand)}
.svc-col{top:1024px}
.svc-head{font-size:10.5px;font-weight:700;color:#2a2a2a;margin-bottom:7px}
.svc-list{list-style:none;font-size:8.6px;line-height:13px;color:#555}
.svc-list li::before{content:"-";margin-right:5px;color:#888}
.net{display:flex;align-items:center;gap:9px;font-size:10.5px;font-weight:700;color:#2a2a2a}
.net-icon{width:20px;height:20px;border-radius:3px;background:var(--brand-light)}
.footer-links{left:183px;top:1165px;font-size:10.4px;color:#555;word-spacing:1px}
.footer-links span{margin:0 9px;color:#777}
.copyright{right:181px;top:1165px;font-size:10.4px;color:#555}
.copyright b{color:var(--brand)}
</style>
</head>
<body>
<header class="header abs"></header>
<div class="brand abs"><div class="brand-mark"></div><div class="brand-name">Marlow Greenery</div></div>
<div class="utility abs">sign in | my account | shopping cart: 0 Items: $0.00</div>
<div class="callout abs">CALL US TODAY!!! <span>555 014 2277</span></div>
<div class="search abs">Search: <div class="search-field">keyword</div><div class="search-go">GO</div></div>

<nav class="nav abs">
  <div class="nav-item active" style="width:86px">HOME</div>
  <div class="nav-item" style="width:116px">HOLIDAY</div>
  <div class="nav-item" style="width:112px">INTERIOR PLANTS</div>
  <div class="nav-item" style="width:116px">INTERIOR DESIGN</div>
  <div class="nav-item" style="width:111px">ONLINE SHOP</div>
  <div class="nav-item" style="width:100px">ABOUT US</div>
  <div class="nav-item" style="width:110px">CONTACT US</div>
</nav>

<main>
<div class="panel abs"></div>
<div class="hero-photo abs" role="img" aria-label="Bright office lounge with orange chairs, glass table and potted plants"></div>
<div class="hero-copy abs"></div>
<div class="hero-kicker abs">Beautiful plants</div>
<div class="hero-title abs">beautiful prices!</div>
<p class="hero-text abs">Beautiful plants at beautiful prices! Corporate or residential interior landscaping! Our ultimate delivery experience is like nothing you have ever experienced! First class service is our standard!</p>
<div class="hero-btn abs">Click here to Design your Planets!
  <svg width="14" height="14" viewBox="0 0 14 14"><circle cx="7" cy="7" r="7" fill="#111"/><path d="M7 3.5v6M4.5 7.5L7 10l2.5-2.5" stroke="#fff" stroke-width="1.5" fill="none"/></svg>
</div>

<h1 class="tagline abs">Inspire our team or create a unique gift.</h1>
<p class="subline abs">We believe in getting it right with great service at the best value.</p>

<div class="steps abs"></div>
<div class="steps-lead abs">See some of our work<br><span>IN 4 EASY STEPS</span></div>
<svg class="abs" style="left:0;top:0" width="1109" height="700" aria-hidden="true">
  <g fill="#0a5a96"><circle cx="546" cy="578" r="19.5"/><circle cx="643" cy="578" r="19.5"/><circle cx="741" cy="578" r="19.5"/><circle cx="840" cy="578" r="19.5"/></g>
  <g fill="#fff" font-family="Carlito,sans-serif" font-weight="700" font-size="21" text-anchor="middle"><text x="546" y="585">1</text><text x="643" y="585">2</text><text x="741" y="585">3</text><text x="840" y="585">4</text></g>
  <g stroke="#222" stroke-width="3.5" fill="none"><path d="M588 572l6 6-6 6"/><path d="M688 572l6 6-6 6"/><path d="M784 572l6 6-6 6"/></g>
</svg>

<h2 class="projects-title abs">Hundreds of Highest-Quality Projects!</h2>
<p class="projects-text abs">Lorem ipsum dolor sit amet, consectetur adipiscing elit. Pellentesque vitae ante est. Proin vel metus viverra nibh egestas ullamcorper. Sed porta, purus ut egestas posuere, diam lectus faucibus justo, vitae malesuada lacus nibh et libero. Etiam quis est sed velit varius tristique. Donec posuere orci sit amet est condimentum aliquam.</p>

<div class="shot abs" style="left:212px;background:linear-gradient(#9b8f9a,#5a3a52 55%,#2c2438)" role="img" aria-label="Hotel lobby decorated with a holiday tree and red chandelier"></div>
<div class="divider abs" style="left:371px"></div>
<div class="shot abs" style="left:394px;background:linear-gradient(#eef0ee,#7f9a5e 50%,#b82a3a 85%,#e6e6e6)" role="img" aria-label="Tall palm in a red planter beside a red chair"></div>
<div class="divider abs" style="left:547px"></div>
<div class="shot abs" style="left:572px;background:linear-gradient(#d8d2c6,#efe8dc 55%,#6a5a4c)" role="img" aria-label="Office desk with an orchid arrangement"></div>
<div class="divider abs" style="left:728px"></div>
<div class="shot abs" style="left:757px;background:linear-gradient(#8a9aa4,#6f8a5c 45%,#e8e8e6)" role="img" aria-label="Bird of paradise plant in a glossy office lobby"></div>
<div class="cta abs">See all Projects</div>
</main>

<section>
<div class="services abs"></div>
<h3 class="services-title abs">Our Services</h3>
<div class="svc-col abs" style="left:196px"><div class="svc-head">Dummy Services</div><ul class="svc-list"><li>Lorem ipsum dolor sit</li><li>consectetur adipiscing elit</li><li>malesuada lacus nibh</li><li>ristique nec mollis</li><li>vitae malesuada lacus</li></ul></div>
<div class="svc-col abs" style="left:343px"><div class="svc-head">Dummy Services</div><ul class="svc-list"><li>Lorem ipsum dolor sit</li><li>consectetur adipiscing elit</li><li>malesuada lacus nibh</li><li>ristique nec mollis</li><li>vitae malesuada lacus</li></ul></div>
<div class="svc-col abs" style="left:483px"><div class="svc-head">Dummy Services</div><ul class="svc-list"><li>Lorem ipsum dolor sit</li><li>consectetur adipiscing elit</li><li>malesuada lacus nibh</li><li>ristique nec mollis</li><li>vitae malesuada lacus</li></ul></div>
<div class="svc-col abs" style="left:639px"><div class="svc-head">Dummy Services</div><ul class="svc-list"><li>Lorem ipsum dolor sit</li><li>consectetur adipiscing elit</li><li>malesuada lacus nibh</li><li>ristique nec mollis</li><li>vitae malesuada lacus</li></ul></div>
<div class="svc-col abs" style="left:794px"><div class="svc-head">Our Networks:</div>
  <div class="net"><div class="net-icon"></div>Friendbook</div>
  <div class="net" style="margin-top:19px"><div class="net-icon"></div>Chirper</div>
</div>
</section>

<footer>
<div class="footer-links abs">Design a Planets<span>|</span>Our Products<span>|</span>Our Services<span>|</span>Online Shop<span>|</span>About Us<span>|</span>Contact Us</div>
<div class="copyright abs">Copyright © 2013 <b>Marlow Greenery</b></div>
</footer>
</body>
</html>
```